Design 5 colour schemes for one web page

We are looking for 5 different colour schemes for our product template to create different kinds of colour tone for our web page, it doesn't need to be restructure the layout, just need to provide different color solution.

Please refer to the attached images and take note of the following when you’re working on the design:
(1) Please precisely reproduce the layout. Cannot remove or delete any wordings, components or column shown in the images.
(2) Okay to revise icons, background color or text style as you prefer. But cannot move/delete them.
(3) Provide PSD source files with good layer management. HTML/CSS are not required.
(4) Make reasonable and professional design.

After completion, please send back:
(1) 5 images with 5 different colour schemes.
(2) Related PSD files.

Industry/Entity Type

Management

Number of Pages Required

1 page

Font styles to use
Serif
Sans Serif

Requirements
Must have
• (1) 5 images for the colour schemes.
• (2) 5 PSD source files with good layer management.
Nice to have
• (1) Explanation about your design of the colour schemes.
Should not have
• (1) HTML/CSS code are not required.

```html
<!DOCTYPE html>
<html lang="en">
<head>
<meta charset="utf-8">
<title>Sports Betting – Today</title>
<link href="https://fonts.googleapis.com/css2?family=Lato:wght@300;400;700;900&display=swap" rel="stylesheet">
<style>
:root{
  --accent:#0f7b5f;
  --accent-dark:#0a5a45;
  --accent-soft:#e3f1ec;
  --bar:#1f2a2e;
  --bar-light:#4a5a5f;
  --grey-bg:#eef1f0;
  --row-alt:#f2f5f4;
  --line:#d3dad8;
  --blue:#1a6fd6;
  --neg:#c62828;
  --badge:#e0862a;
  --text:#333;
}
*{box-sizing:border-box;margin:0;padding:0}
html,body{width:1200px;height:1200px;overflow:hidden;background:var(--grey-bg)}
body{font-family:'Lato',sans-serif;color:var(--text)}
.page{width:1400px;height:1400px;position:relative;transform:scale(.857143);transform-origin:0 0;background:var(--grey-bg)}
.abs{position:absolute}

/* top bar */
.topbar{left:0;top:0;width:1400px;height:53px;background:linear-gradient(#2b3538,#182023);color:#fff;font-size:13px;font-weight:700;text-transform:uppercase;white-space:nowrap}
.topbar .nav{left:201px;top:19px;display:flex;gap:30px}
.badge{background:var(--badge);border-radius:4px;padding:5px 6px;margin-top:-6px;font-size:12px}
.user{left:823px;top:19px}
.wallet{left:917px;top:12px;width:186px;height:28px;background:#0f1517;padding:7px 12px;display:flex;justify-content:space-between}
.signout{left:1110px;top:12px;width:90px;height:28px;background:#0f1517;padding:7px 0;text-align:center}

/* header */
.header{left:0;top:53px;width:1400px;height:106px;background:var(--accent)}
.logo{left:198px;top:18px;font-size:60px;font-weight:300;color:#fff;letter-spacing:1px}
.tab-sports{left:462px;top:51px;width:118px;height:55px;background:linear-gradient(#f4f4f4,#cfd5d3);border-radius:4px 4px 0 0;text-align:center;padding-top:19px;font-weight:700;font-size:15px;color:#444}
.results{left:1094px;top:13px;width:106px;height:27px;background:var(--accent-dark);color:#fff;font-weight:700;font-size:14px;padding:5px 10px;display:flex;gap:8px;align-items:center;text-decoration:underline}

/* toolbar */
.toolbar{left:0;top:159px;width:1400px;height:41px;background:linear-gradient(#f3f5f4,#dde2e0);font-size:12px;color:#555;white-space:nowrap}
.toolbar .lang{left:201px;top:12px;display:flex;gap:8px;align-items:center}
.toolbar .date{left:333px;top:4px;height:32px;border-left:1px solid #ccc;padding:9px 18px}
.tools{left:860px;top:4px;display:flex}
.tools span{height:32px;border-left:1px solid #ccc;padding:9px 14px;font-size:11px;color:#555}

/* sidebar */
.panel{background:#fff;box-shadow:0 1px 2px rgba(0,0,0,.12)}
.panel-head{background:var(--bar);color:#fff;font-weight:700;font-size:12px;text-transform:uppercase;text-align:center}
.fav{left:200px;top:214px;width:184px;height:119px;background:#e8ecea}
.fav .panel-head{height:42px;padding-top:15px}
.fav-note{margin:16px 15px;border:1px dashed #bbb;padding:6px 2px;font-size:11.5px;color:#999;text-align:center;line-height:14px;white-space:nowrap}
.sports{left:200px;top:349px;width:184px;height:661px}
.tabs{display:flex;height:38px;font-weight:700;font-size:12px;white-space:nowrap}
.tabs div{flex:1;text-align:center;padding-top:14px}
.tabs .on{color:var(--accent)}
.tabs .off{background:var(--accent);color:#fff}
.sport-list{list-style:none;padding-top:8px}
.sport-list li{height:30px;display:flex;align-items:center;padding-left:15px;font-size:12.5px;color:#444;white-space:nowrap}
.sport-list li svg{width:15px;height:15px;margin-right:6px;flex:none}
.sport-list li b{margin-left:auto;margin-right:12px;font-weight:400}
.ticket{left:200px;top:1026px;width:184px;height:52px}
.ticket .tabs{height:40px}
.parlay-count{background:#fff;color:var(--accent);border-radius:4px;padding:0 4px;margin-left:3px}
.mybets{left:200px;top:1093px;width:184px;height:178px}
.mybets .panel-head{height:42px;padding-top:15px}
.refresh{text-align:center;margin-top:16px;color:var(--accent);font-size:14px;display:flex;justify-content:center;gap:5px;align-items:center}
.pending{margin:14px 12px 0;background:#e4e8e6;height:27px;text-align:center;padding-top:5px;font-size:14px}
.viewall{position:absolute;left:0;bottom:0;width:184px;height:42px;background:var(--accent);color:#fff;font-weight:700;font-size:13px;text-align:center;padding-top:13px}

/* odds tables */
.board{left:391px;width:809px}
.board-head{height:44px;background:var(--bar);color:#fff;display:flex;align-items:center;padding:0 10px 0 12px;font-weight:700;font-size:15px;text-transform:uppercase;white-space:nowrap}
.board-head .count{margin-left:auto;margin-right:auto;padding-left:40px;display:flex;gap:6px;align-items:center;text-transform:none}
.board-head .league-pick{font-size:12px;display:flex;gap:5px;align-items:center}
.grid{display:grid;grid-template-columns:64px 181px 44px 75px 104px 51px 76px 104px 52px 58px}
.cols{background:var(--accent);color:#fff;font-weight:700;font-size:12px;height:37px;grid-template-rows:16px 21px;white-space:nowrap}
.cols>div{border-right:1px solid rgba(255,255,255,.35);display:flex;align-items:center;justify-content:center}
.cols>div:last-child{border-right:0}
.cols .h-time{grid-column:1;grid-row:1/3}
.cols .h-event{grid-column:2;grid-row:1/3}
.cols .h-full{grid-column:3/7;grid-row:1;border-bottom:1px solid rgba(255,255,255,.35)}
.cols .h-half{grid-column:7/10;grid-row:1;border-bottom:1px solid rgba(255,255,255,.35)}
.cols .h-more{grid-column:10;grid-row:1/3}
.cols .sub{grid-row:2}
.league{height:27px;display:flex;align-items:center;justify-content:space-between;padding:0 18px 0 70px;color:#fff;font-weight:700;font-size:12.5px}
.league.accent{background:var(--accent)}
.league.dark{background:var(--bar-light)}
.league span{display:flex;gap:6px;align-items:center}
.match{height:54px;background:#fff;border-bottom:1px solid #e2e6e4;font-size:12px;font-weight:700;white-space:nowrap}
.match.alt{background:var(--row-alt)}
.match.live{height:36px;background:#e5eae8}
.match>div{border-right:1px solid var(--line);padding-top:5px;line-height:15px;position:relative}
.match>div:last-child{border-right:0}
.c-time{padding-left:28px}
.c-time .stat{position:absolute;left:6px;top:13px;width:13px;height:13px;background:#5c6664}
.c-time i{display:block;color:var(--accent);padding-left:10px}
.c-event{padding-left:25px}
.c-event .star{position:absolute;left:6px;top:12px;color:#888}
.home{color:#333}.away{color:var(--accent)}.draw{color:#333}
.c-hdp{padding:5px 4px 0 4px}
.r{text-align:right}
.blue{color:var(--blue)}.neg{color:var(--neg)}
.pair{display:flex;justify-content:space-between}
.c-ou{padding:5px 4px 0 5px}
.ou-line{display:grid;grid-template-columns:40px 24px 1fr}
.ou-line em{font-style:normal;font-weight:400;color:#555;text-align:center}
.more{padding:10px 7px 0 6px !important}
.more span{display:block;background:#e3e8e6;border-radius:3px;height:24px;text-align:center;padding-top:4px;font-size:12px}
.match.live .more{padding-top:5px !important}

/* footer */
.footer{left:0;top:1304px;width:1400px;height:96px;background:#232b2d;color:#9aa3a1;font-size:14px;white-space:nowrap}
.footer .copy{left:199px;top:40px}
.footer .links{right:202px;top:40px;display:flex;gap:18px}
</style>
</head>
<body>
<div class="page">

<div class="abs topbar">
  <div class="abs nav"><span>My Bets</span><span>Statement</span><span>Preference</span><span>Announcements</span><span class="badge">99+</span></div>
  <div class="abs user">Hi, STWTG036</div>
  <div class="abs wallet"><span>›› SD$</span><span>10,072.00 ↻</span></div>
  <div class="abs signout">Sign Out</div>
</div>

<div class="abs header">
  <div class="abs logo">LOGO</div>
  <div class="abs tab-sports">SPORTS</div>
  <div class="abs results"><svg width="16" height="14" viewBox="0 0 16 14"><path d="M3 1h10v3a5 5 0 0 1-10 0z M1 2h2v2H1z M13 2h2v2h-2z M7 9h2v3H7z M5 12h6v2H5z" fill="#fff"/></svg>RESULTS</div>
</div>

<div class="abs toolbar">
  <div class="abs lang"><svg width="15" height="15" viewBox="0 0 16 16"><circle cx="8" cy="8" r="7" fill="#888"/></svg>English (Asia)</div>
  <div class="abs date">12/02/2013 15:53PM GMT+8</div>
  <div class="abs tools"><span>⊞ ▾</span><span>★ ▾</span><span>☰ ▾</span><span>MY ▾</span><span>◀)</span><span>▭</span><span>Live</span></div>
</div>

<div class="abs fav">
  <div class="panel-head">My Favourites</div>
  <div class="fav-note">Click o an event or league<br>to add it to "My Favourites"</div>
</div>

<div class="abs panel sports">
  <div class="tabs"><div class="on">SPORTS</div><div class="off">MARKETS</div></div>
  <ul class="sport-list">
    <li><svg viewBox="0 0 16 16"><circle cx="8" cy="8" r="6.5" fill="none" stroke="#555" stroke-width="2"/></svg>Football<b>600</b></li>
    <li><svg viewBox="0 0 16 16"><circle cx="8" cy="8" r="6.5" fill="none" stroke="#555" stroke-width="2"/></svg>Basketball<b>600</b></li>
    <li><svg viewBox="0 0 16 16"><circle cx="8" cy="8" r="6.5" fill="none" stroke="#555" stroke-width="2"/></svg>Baseball<b>600</b></li>
    <li><svg viewBox="0 0 16 16"><circle cx="8" cy="8" r="6.5" fill="#555"/></svg>Tennis<b>600</b></li>
    <li><svg viewBox="0 0 16 16"><circle cx="8" cy="8" r="6.5" fill="#555"/></svg>American Football<b>600</b></li>
    <li><svg viewBox="0 0 16 16"><path d="M3 13 L13 3 L14 8 Z" fill="#555"/></svg>Badminton<b>600</b></li>
    <li><svg viewBox="0 0 16 16"><circle cx="6" cy="8" r="4" fill="#555"/><circle cx="11" cy="8" r="4" fill="#555"/></svg>Boxing<b>600</b></li>
    <li><svg viewBox="0 0 16 16"><path d="M10 2 L12 3 L6 14 L4 13 Z" fill="#555"/></svg>Cricket<b>600</b></li>
    <li><svg viewBox="0 0 16 16"><circle cx="4" cy="11" r="3" fill="none" stroke="#555" stroke-width="1.5"/><circle cx="12" cy="11" r="3" fill="none" stroke="#555" stroke-width="1.5"/></svg>Cycling<b>600</b></li>
    <li><svg viewBox="0 0 16 16"><path d="M2 2 L14 14" stroke="#555" stroke-width="3"/></svg>Darts<b>600</b></li>
    <li><svg viewBox="0 0 16 16"><rect x="4" y="2" width="8" height="12" rx="2" fill="#555"/></svg>Entertainment<b>600</b></li>
    <li><svg viewBox="0 0 16 16"><path d="M7 1v12M7 1l6 3-6 3" stroke="#555" stroke-width="2" fill="#555"/><rect x="2" y="13" width="12" height="2" fill="#555"/></svg>Golf<b>600</b></li>
    <li><svg viewBox="0 0 16 16"><circle cx="8" cy="8" r="6.5" fill="none" stroke="#555" stroke-width="2"/></svg>Handball<b>600</b></li>
    <li><svg viewBox="0 0 16 16"><path d="M4 2 L8 12 H14" stroke="#555" stroke-width="2" fill="none"/></svg>Ice Hockey<b>600</b></li>
    <li><svg viewBox="0 0 16 16"><circle cx="8" cy="3" r="2" fill="#555"/><path d="M8 5 L5 15 M8 5 L11 15" stroke="#555" stroke-width="2"/></svg>Mixed Martial Arts<b>600</b></li>
    <li><svg viewBox="0 0 16 16"><circle cx="8" cy="8" r="6" fill="none" stroke="#555" stroke-width="2.5"/></svg>Motor Sport<b>600</b></li>
    <li><svg viewBox="0 0 16 16"><path d="M8 2 L14 14 H2 Z" fill="#555"/></svg>Pool/Snooker<b>600</b></li>
    <li><svg viewBox="0 0 16 16"><circle cx="9" cy="3" r="2" fill="#555"/><path d="M9 5 L6 15 M9 5 L13 14" stroke="#555" stroke-width="2"/></svg>Rugby<b>600</b></li>
    <li><svg viewBox="0 0 16 16"><circle cx="9" cy="3" r="2" fill="#555"/><path d="M9 5 L7 15" stroke="#555" stroke-width="2"/></svg>Volleyball<b>600</b></li>
    <li><svg viewBox="0 0 16 16"><circle cx="8" cy="3" r="2" fill="#555"/><path d="M8 5 L6 12 M2 14 H14" stroke="#555" stroke-width="2"/></svg>Winter Sports<b>600</b></li>
  </ul>
</div>

<div class="abs panel ticket">
  <div class="tabs"><div class="on">TICKET</div><div class="off">PARLAY <span class="parlay-count">0</span></div></div>
</div>

<div class="abs panel mybets">
  <div class="panel-head">My Bets</div>
  <div class="refresh"><svg width="14" height="14" viewBox="0 0 16 16"><path d="M13 8a5 5 0 1 1-2-4" stroke="#333" stroke-width="2" fill="none"/></svg>Refresh</div>
  <div class="pending">No pending bets</div>
  <div class="viewall">View All</div>
</div>

<div class="abs board" style="top:214px">
  <div class="board-head">🏃&#xFE0E; Today - Live<span class="count">↻ 38</span><span class="league-pick">🏆&#xFE0E; SELECT LEAGUE</span></div>
  <div class="grid cols">
    <div class="h-time">Time</div><div class="h-event">Event</div>
    <div class="h-full">Full Time</div><div class="h-half">First Half</div><div class="h-more">+ More</div>
    <div class="sub">A 1x2</div><div class="sub">HDP</div><div class="sub">OU</div><div class="sub">1X2</div><div class="sub">HDP</div><div class="sub">OU</div><div class="sub">1X2</div>
  </div>
  <div class="league accent"><span>★ Coastal Premier League</span><span>↻</span></div>
  <div class="grid match live">
    <div class="c-time"><span class="stat"></span>16.30<i>Live</i></div>
    <div class="c-event"><span class="star">☆</span><div class="home">Bayside Harbour Mariners</div><div class="away">Riverside Victory</div></div>
    <div></div>
    <div class="c-hdp"><div class="r">0.77</div><div class="pair"><span class="blue">0-0.5</span><span class="neg">-0.95</span></div></div>
    <div class="c-ou"><div class="pair"><span class="blue">6-6.5</span><span class="neg">-0.85</span></div><div class="r">0.65</div></div>
    <div></div><div></div><div></div><div></div>
    <div class="more"><span>⇕13</span></div>
  </div>
</div>

<div class="abs board" style="top:380px">
  <div class="board-head">🏃&#xFE0E; Today - Non-Live<span class="count">↻ 38</span><span class="league-pick">🏆&#xFE0E; SELECT LEAGUE</span></div>
  <div class="grid cols">
    <div class="h-time">Time</div><div class="h-event">Event</div>
    <div class="h-full">Full Time</div><div class="h-half">First Half</div><div class="h-more">+ More</div>
    <div class="sub">A 1x2</div><div class="sub">HDP</div><div class="sub">OU</div><div class="sub">1X2</div><div class="sub">HDP</div><div class="sub">OU</div><div class="sub">1X2</div>
  </div>

  <div class="league dark"><span>★ Coastal Premier League</span><span>↻</span></div>
  <div class="grid match"><div class="c-time"><span class="stat"></span>16.30<i>Live</i></div><div class="c-event"><span class="star">☆</span><div class="home">Bayside Harbour Mariners</div><div class="away">Riverside Victory</div><div class="draw">Draw</div></div><div></div><div class="c-hdp"><div class="r">0.77</div><div class="pair"><span class="blue">0-0.5</span><span class="neg">-0.95</span></div></div><div class="c-ou"><div class="ou-line"><span class="blue">6-6.5</span><em>o</em><span class="neg r">-0.85</span></div><div class="ou-line"><span></span><em>u</em><span class="r">0.65</span></div></div><div></div><div></div><div></div><div></div><div class="more"><span>⇕13</span></div></div>

  <div class="league accent"><span>★ Coastal Premier League</span><span>↻</span></div>
  <div class="grid match"><div class="c-time"><span class="stat"></span>16.30<i>Live</i></div><div class="c-event"><span class="star">☆</span><div class="home">Bayside Harbour Mariners</div><div class="away">Riverside Victory</div><div class="draw">Draw</div></div><div></div><div class="c-hdp"><div class="r">0.77</div><div class="pair"><span class="blue">0-0.5</span><span class="neg">-0.95</span></div></div><div class="c-ou"><div class="ou-line"><span class="blue">6-6.5</span><em>o</em><span class="neg r">-0.85</span></div><div class="ou-line"><span></span><em>u</em><span class="r">0.65</span></div></div><div></div><div></div><div></div><div></div><div class="more"><span>⇕13</span></div></div>
  <div class="grid match alt"><div class="c-time"><span class="stat"></span>16.30<i>Live</i></div><div class="c-event"><span class="star">☆</span><div class="home">Bayside Harbour Mariners</div><div class="away">Riverside Victory</div><div class="draw">Draw</div></div><div></div><div class="c-hdp"><div class="r">0.77</div><div class="pair"><span class="blue">0-0.5</span><span class="neg">-0.95</span></div></div><div class="c-ou"><div class="ou-line"><span class="blue">6-6.5</span><em>o</em><span class="neg r">-0.85</span></div><div class="ou-line"><span></span><em>u</em><span class="r">0.65</span></div></div><div></div><div></div><div></div><div></div><div class="more"><span>⇕13</span></div></div>
  <div class="grid match"><div class="c-time"><span class="stat"></span>16.30<i>Live</i></div><div class="c-event"><span class="star">☆</span><div class="home">Bayside Harbour Mariners</div><div class="away">Riverside Victory</div><div class="draw">Draw</div></div><div></div><div class="c-hdp"><div class="r">0.77</div><div class="pair"><span class="blue">0-0.5</span><span class="neg">-0.95</span></div></div><div class="c-ou"><div class="ou-line"><span class="blue">6-6.5</span><em>o</em><span class="neg r">-0.85</span></div><div class="ou-line"><span></span><em>u</em><span class="r">0.65</span></div></div><div></div><div></div><div></div><div></div><div class="more"><span>⇕13</span></div></div>

  <div class="league accent"><span>★ Coastal Premier League</span><span>↻</span></div>
  <div class="grid match"><div class="c-time"><span class="stat"></span>16.30<i>Live</i></div><div class="c-event"><span class="star">☆</span><div class="home">Bayside Harbour Mariners</div><div class="away">Riverside Victory</div><div class="draw">Draw</div></div><div></div><div class="c-hdp"><div class="r">0.77</div><div class="pair"><span class="blue">0-0.5</span><span class="neg">-0.95</span></div></div><div class="c-ou"><div class="ou-line"><span class="blue">6-6.5</span><em>o</em><span class="neg r">-0.85</span></div><div class="ou-line"><span></span><em>u</em><span class="r">0.65</span></div></div><div></div><div></div><div></div><div></div><div class="more"><span>⇕13</span></div></div>

  <div class="league accent"><span>★ Coastal Premier League</span><span>↻</span></div>
  <div class="grid match"><div class="c-time"><span class="stat"></span>16.30<i>Live</i></div><div class="c-event"><span class="star">☆</span><div class="home">Bayside Harbour Mariners</div><div class="away">Riverside Victory</div><div class="draw">Draw</div></div><div></div><div class="c-hdp"><div class="r">0.77</div><div class="pair"><span class="blue">0-0.5</span><span class="neg">-0.95</span></div></div><div class="c-ou"><div class="ou-line"><span class="blue">6-6.5</span><em>o</em><span class="neg r">-0.85</span></div><div class="ou-line"><span></span><em>u</em><span class="r">0.65</span></div></div><div></div><div></div><div></div><div></div><div class="more"><span>⇕13</span></div></div>
  <div class="grid match alt"><div class="c-time"><span class="stat"></span>16.30<i>Live</i></div><div class="c-event"><span class="star">☆</span><div class="home">Bayside Harbour Mariners</div><div class="away">Riverside Victory</div><div class="draw">Draw</div></div><div></div><div class="c-hdp"><div class="r">0.77</div><div class="pair"><span class="blue">0-0.5</span><span class="neg">-0.95</span></div></div><div class="c-ou"><div class="ou-line"><span class="blue">6-6.5</span><em>o</em><span class="neg r">-0.85</span></div><div class="ou-line"><span></span><em>u</em><span class="r">0.65</span></div></div><div></div><div></div><div></div><div></div><div class="more"><span>⇕13</span></div></div>
  <div class="grid match"><div class="c-time"><span class="stat"></span>16.30<i>Live</i></div><div class="c-event"><span class="star">☆</span><div class="home">Bayside Harbour Mariners</div><div class="away">Riverside Victory</div><div class="draw">Draw</div></div><div></div><div class="c-hdp"><div class="r">0.77</div><div class="pair"><span class="blue">0-0.5</span><span class="neg">-0.95</span></div></div><div class="c-ou"><div class="ou-line"><span class="blue">6-6.5</span><em>o</em><span class="neg r">-0.85</span></div><div class="ou-line"><span></span><em>u</em><span class="r">0.65</span></div></div><div></div><div></div><div></div><div></div><div class="more"><span>⇕13</span></div></div>
  <div class="grid match alt"><div class="c-time"><span class="stat"></span>16.30<i>Live</i></div><div class="c-event"><span class="star">☆</span><div class="home">Bayside Harbour Mariners</div><div class="away">Riverside Victory</div><div class="draw">Draw</div></div><div></div><div class="c-hdp"><div class="r">0.77</div><div class="pair"><span class="blue">0-0.5</span><span class="neg">-0.95</span></div></div><div class="c-ou"><div class="ou-line"><span class="blue">6-6.5</span><em>o</em><span class="neg r">-0.85</span></div><div class="ou-line"><span></span><em>u</em><span class="r">0.65</span></div></div><div></div><div></div><div></div><div></div><div class="more"><span>⇕13</span></div></div>
  <div class="grid match"><div class="c-time"><span class="stat"></span>16.30<i>Live</i></div><div class="c-event"><span class="star">☆</span><div class="home">Bayside Harbour Mariners</div><div class="away">Riverside Victory</div><div class="draw">Draw</div></div><div></div><div class="c-hdp"><div class="r">0.77</div><div class="pair"><span class="blue">0-0.5</span><span class="neg">-0.95</span></div></div><div class="c-ou"><div class="ou-line"><span class="blue">6-6.5</span><em>o</em><span class="neg r">-0.85</span></div><div class="ou-line"><span></span><em>u</em><span class="r">0.65</span></div></div><div></div><div></div><div></div><div></div><div class="more"><span>⇕13</span></div></div>
  <div class="grid match alt"><div class="c-time"><span class="stat"></span>16.30<i>Live</i></div><div class="c-event"><span class="star">☆</span><div class="home">Bayside Harbour Mariners</div><div class="away">Riverside Victory</div><div class="draw">Draw</div></div><div></div><div class="c-hdp"><div class="r">0.77</div><div class="pair"><span class="blue">0-0.5</span><span class="neg">-0.95</span></div></div><div class="c-ou"><div class="ou-line"><span class="blue">6-6.5</span><em>o</em><span class="neg r">-0.85</span></div><div class="ou-line"><span></span><em>u</em><span class="r">0.65</span></div></div><div></div><div></div><div></div><div></div><div class="more"><span>⇕13</span></div></div>
  <div class="grid match"><div class="c-time"><span class="stat"></span>16.30<i>Live</i></div><div class="c-event"><span class="star">☆</span><div class="home">Bayside Harbour Mariners</div><div class="away">Riverside Victory</div><div class="draw">Draw</div></div><div></div><div class="c-hdp"><div class="r">0.77</div><div class="pair"><span class="blue">0-0.5</span><span class="neg">-0.95</span></div></div><div class="c-ou"><div class="ou-line"><span class="blue">6-6.5</span><em>o</em><span class="neg r">-0.85</span></div><div class="ou-line"><span></span><em>u</em><span class="r">0.65</span></div></div><div></div><div></div><div></div><div></div><div class="more"><span>⇕13</span></div></div>
  <div class="grid match alt"><div class="c-time"><span class="stat"></span>16.30<i>Live</i></div><div class="c-event"><span class="star">☆</span><div class="home">Bayside Harbour Mariners</div><div class="away">Riverside Victory</div><div class="draw">Draw</div></div><div></div><div class="c-hdp"><div class="r">0.77</div><div class="pair"><span class="blue">0-0.5</span><span class="neg">-0.95</span></div></div><div class="c-ou"><div class="ou-line"><span class="blue">6-6.5</span><em>o</em><span class="neg r">-0.85</span></div><div class="ou-line"><span></span><em>u</em><span class="r">0.65</span></div></div><div></div><div></div><div></div><div></div><div class="more"><span>⇕13</span></div></div>
</div>

<div class="abs footer">
  <div class="abs copy">© 2014. All Rights Reserved.</div>
  <div class="abs links"><span>Betting Rules</span><span>Contact Us</span><span>Privacy Policy</span><span>Responsible Gamnling</span><span>Terms &amp; Conditions</span><span>Tutorials</span></div>
</div>

</div>
</body>
</html>
```